New Flyer Design Project

PAGE 1

Change to 8th Annual Ridgeback Clash and the new date is January 24, 2026

12U, Middle School & High School - add Open 18+

Under Weigh-ins
Early Registration is $25.00
Deadline is January 18, 2026 at 11:59 PM

Regular Registration is $35.00
Deadline is January 21, 2026 at 11:59 PM

Late / On-site Registration is $50.00
Deadline is January 23, 2026 at 5:00 PM
Change 500 to 750

Under Weigh-Ins - Change
January 24, 2025 to January 23, 2026
January 25, 2025 to January 24, 2026

PAGE 2
Change 2024-2025 to 2025-2026

In the Division Line Fix the numbers 1, 2, 3, 4, 5, 6, 7, 8, 9, 10

Change 12/31/2024 to 12/31/2025 where it says "Age As Of"
Change to "Excluding the High School & Open Division"

```html
<!DOCTYPE html>
<html lang="en">
<head>
<meta charset="utf-8">
<title>8th Annual Ridgeback Clash – Flyer</title>
<link href="https://fonts.googleapis.com/css2?family=Anton&family=Bebas+Neue&family=Oswald:wght@400;500;600&family=Poppins:wght@400;600;700&display=swap" rel="stylesheet">
<style>
:root{
  --bg:#b9b9b9;
  --maroon:#6e0f14;
  --deep:#430a0d;
  --wine:#7d1119;
  --gold:#d9962e;
  --gold-light:#f1bf5c;
  --cream:#fde9cb;
  --peach:#f3b46a;
  --cell:#f7dfae;
  --cell-head:#e39a3a;
  --ink:#2a0709;
  --white:#ffffff;
}
*{margin:0;padding:0;box-sizing:border-box}
html,body{width:1200px;height:945px;overflow:hidden;background:var(--bg)}
.page{position:absolute;top:113px;width:514px;height:719px;overflow:hidden;
  background:linear-gradient(180deg,var(--cream) 0%,#fbd9a6 45%,var(--peach) 100%);
  font-family:"Poppins",sans-serif;color:var(--white)}
.page--front{left:68px}
.page--back{left:619px}
.abs{position:absolute}

/* headline */
.headline-top{font-family:"Anton",sans-serif;color:var(--maroon);font-size:58px;line-height:1;letter-spacing:-.5px;
  text-shadow:2px 2px 0 var(--ink),-1px -1px 0 #fff}
.headline-sub{font-family:"Anton",sans-serif;color:var(--white);font-size:34px;line-height:1;letter-spacing:-.3px;
  text-shadow:-2px 0 var(--maroon),2px 0 var(--maroon),0 -2px var(--maroon),0 2px var(--maroon),3px 3px 0 var(--ink)}

/* org tab */
.org-tab{left:371px;top:0;width:106px;height:123px;background:var(--maroon);border-radius:0 0 53px 53px;
  display:flex;flex-direction:column;align-items:center;padding-top:30px;gap:6px}
.org-name{font-family:"Oswald",sans-serif;font-weight:600;font-size:22px;color:var(--white);display:flex;align-items:center;gap:6px}
.org-dot{width:10px;height:10px;border-radius:50%;background:var(--white)}
.org-tag{font-family:"Poppins",sans-serif;font-weight:700;font-size:5.6px;text-align:center;line-height:1.3;text-transform:uppercase;width:86px}

/* date bar */
.date-bar{left:36px;top:131px;display:flex;height:28px;font-family:"Oswald",sans-serif;font-weight:500;font-size:19px}
.date-bar span{display:flex;align-items:center;padding:0 9px;background:var(--maroon)}
.date-bar .date-month{background:var(--ink);padding:0 13px}

.venue{left:36px;top:169px;display:flex;gap:8px;color:var(--ink);font-weight:700;font-size:11.5px;line-height:1.15}

.photo{background:linear-gradient(160deg,#b88a5a 0%,#6d2a1c 35%,#3b1a12 70%,#20100c 100%)}
.photo--front{left:290px;top:190px;width:224px;height:507px;z-index:1;
  background:radial-gradient(ellipse at 60% 30%,#8a6a4a 0%,#5a1c16 35%,#3a1b14 65%,#1f0f0b 100%)}

.band{left:0;width:312px;z-index:2}
.band--gold{top:202px;height:79px;background:linear-gradient(90deg,var(--gold) 0%,var(--gold-light) 100%);
  font-family:"Bebas Neue",sans-serif;font-size:11.5px;color:var(--ink);text-transform:uppercase}
.band-row{position:absolute;left:36px;height:18px;line-height:18px;white-space:nowrap}
.band-row--1{top:5px}
.band-row--2{top:27px;left:36px}
.band-row--3{top:50px}
.tag{display:inline-block;background:var(--maroon);color:var(--white);padding:0 8px;margin-right:5px;line-height:17px}
.tag--dark{display:inline-block;background:var(--ink);color:var(--white);padding:0 8px;line-height:17px}
.hl{color:var(--maroon)}

.band--red{top:285px;height:165px;background:var(--wine)}
.fees{position:absolute;left:36px;top:12px}
.fee{width:244px;height:33px;margin-bottom:4px;padding:3px 0 0 6px;position:relative;
  border:1px solid rgba(255,255,255,.55);border-left:none;border-top:none;border-radius:0 6px 6px 0}
.fee::before{content:"";position:absolute;left:0;top:2px;bottom:2px;width:1px;background:rgba(255,255,255,.8)}
.fee-title{font-family:"Oswald",sans-serif;font-size:13px;font-variant:small-caps;font-weight:500;line-height:1.2}
.fee-title b{color:var(--gold-light);font-weight:500}
.fee-note{font-size:8px;line-height:1.2}
.limit{position:absolute;left:36px;top:126px;font-family:"Oswald",sans-serif;font-size:10.5px;text-transform:uppercase;white-space:nowrap}
.limit b{color:var(--gold-light);font-weight:500}
.limit-note{position:absolute;left:36px;top:142px;font-size:6.5px;white-space:nowrap}

.band--deep{top:451px;height:246px;background:var(--deep)}
.band--deep > *{position:absolute;left:36px}
.weigh-tag{top:14px;background:var(--gold);color:var(--ink);font-family:"Oswald",sans-serif;font-size:10.5px;padding:2px 6px;line-height:1.3}
.weigh-list{top:38px;left:32px;width:268px;list-style:none;font-family:"Oswald",sans-serif;font-size:8.2px;text-transform:uppercase;white-space:nowrap}
.weigh-list li{height:17px;line-height:16px;border-bottom:1px solid rgba(255,255,255,.25)}
.weigh-list li span{color:var(--gold-light)}
.fine{font-size:6.3px;line-height:1.25;width:250px}
.fine--1{top:91px}
.fine--2{top:121px}
.admission{top:156px;display:flex;gap:6px;align-items:center;font-family:"Oswald",sans-serif;font-size:7.5px;text-transform:uppercase;white-space:nowrap}
.admission .tag{background:var(--gold);color:var(--ink);padding:0 4px;margin:0;line-height:12px}
.contact{top:174px;display:flex;align-items:center;gap:5px;font-family:"Oswald",sans-serif;text-transform:uppercase;white-space:nowrap}
.contact-label{font-size:7.6px;line-height:1.15}
.contact-label span{color:var(--gold-light)}
.contact-phone{font-size:17px;font-weight:500;line-height:1}
.hotels-title{top:209px;font-family:"Oswald",sans-serif;font-size:7.5px;text-transform:uppercase;white-space:nowrap}
.hotels{top:224px;display:flex;gap:3px;font-family:"Bebas Neue",sans-serif;font-size:8px;text-transform:uppercase;white-space:nowrap}
.hotels span{padding:0 3px;line-height:11px;background:var(--white);color:var(--ink)}
.hotels span.h-name{background:var(--gold);color:var(--white)}

.strip{left:0;top:697px;width:514px;height:22px;z-index:2;background:linear-gradient(90deg,var(--gold-light),var(--gold))}

.open-badge{left:340px;top:296px;width:68px;height:68px;border-radius:50%;background:var(--maroon);border:2px solid var(--cream);
  z-index:3;display:flex;flex-direction:column;align-items:center;justify-content:center;font-family:"Oswald",sans-serif;font-weight:500;line-height:1}
.open-badge .o1{font-size:17px;font-variant:small-caps}
.open-badge .o2{font-size:19px;color:var(--gold-light)}

/* back page */
.title-block{left:130px;top:35px}
.panel{left:37px;top:126px;width:440px;height:361px;background:var(--maroon);border-radius:12px 12px 0 0}
.panel-title{left:37px;top:129px;width:440px;text-align:center;font-family:"Oswald",sans-serif;font-size:11px;color:var(--white)}
.panel-title b{color:var(--gold-light);font-weight:500}
.col{position:absolute;top:148px;width:34px;display:flex;flex-direction:column;align-items:stretch}
.cell-num{height:12px;background:var(--maroon);border:1px solid var(--gold);border-radius:2px;font-family:"Oswald",sans-serif;font-size:7px;
  display:flex;align-items:center;justify-content:center}
.cell-label{height:25px;margin-top:3px;background:var(--cell-head);border-radius:2px;color:var(--white);font-size:3.6px;font-weight:700;
  text-transform:uppercase;display:flex;align-items:center;justify-content:center;text-align:center;line-height:1.2;padding:1px}
.cells{margin-top:1.6px;display:flex;flex-direction:column;gap:2.9px}
.cells span{height:12px;background:var(--cell);border-radius:2px;color:var(--ink);font-size:5.6px;display:flex;align-items:center;justify-content:center}
.cells span.blank{background:#f9e6c0}
.cell-label--first{justify-content:flex-start;text-align:left;font-size:3.4px}

.photo--mats{left:69px;top:487px;width:445px;height:132px;background:linear-gradient(180deg,#6b5a4a 0%,#3d4448 40%,#2c3336 100%)}
.photo--back{left:0;top:367px;width:137px;height:352px;z-index:2;
  background:radial-gradient(ellipse at 50% 30%,#8a6a4a 0%,#5a1c16 40%,#2a1410 100%)}
.band--award{left:0;top:619px;width:514px;height:100px;background:var(--wine)}
.award-text{left:161px;top:633px;width:170px;font-family:"Oswald",sans-serif;font-size:10.3px;line-height:1.2;text-transform:uppercase;z-index:3}
.award-text span{color:var(--gold-light)}
.singlet{top:606px;width:63px;height:78px;border-radius:8px;border:2px solid var(--gold);z-index:3;
  background:linear-gradient(180deg,#e8dcc6,#b9a88e)}
.singlet--a{left:345px}
.singlet--b{left:413px;background:linear-gradient(180deg,#cfc6b8,#6e0f14)}
</style>
</head>
<body>

<section class="page page--front">
  <div class="abs org-tab">
    <div class="org-name"><span class="org-dot"></span>CWL</div>
    <div class="org-tag">Carolina's Premier<br>Wrestling League</div>
  </div>

  <div class="abs headline-top" style="left:36px;top:35px">8TH ANNUAL</div>
  <div class="abs headline-sub" style="left:36px;top:94px">RIDGEBACK CLASH</div>

  <div class="abs date-bar"><span>24TH</span><span class="date-month">JANUARY</span><span>2026</span></div>

  <div class="abs venue">
    <svg width="11" height="14" viewBox="0 0 11 14"><path d="M5.5 0C2.5 0 0 2.4 0 5.4 0 9.3 5.5 14 5.5 14S11 9.3 11 5.4C11 2.4 8.5 0 5.5 0z" fill="#6e0f14"/><circle cx="5.5" cy="5.3" r="2" fill="#fde9cb"/></svg>
    <div>Harbor Point Event Center<br>410 Eastline Ave, Riverton, NC</div>
  </div>

  <div class="abs photo photo--front" role="img" aria-label="Armored warrior with crested helmet and spear"></div>

  <div class="abs band band--gold">
    <div class="band-row band-row--1"><span class="tag">6 MATS</span>K-5, 6U, 8U, 10U – <span class="hl">Wrestling starts at 8:30 AM</span></div>
    <div class="band-row band-row--2">12U, Middle School, High School &amp; Open 18+ – <span class="hl">Wrestling starts at 1:00 PM</span></div>
    <div class="band-row band-row--3"><span class="tag">REGISTER</span><span class="tag--dark">@ WWW.MATSCOREONLINE.COM</span></div>
  </div>

  <div class="abs band band--red">
    <div class="fees">
      <div class="fee"><div class="fee-title">Early Registration is <b>$25.00</b></div><div class="fee-note">Deadline is January 18, 2026 at 11:59 PM</div></div>
      <div class="fee"><div class="fee-title">Regular Registration is <b>$35.00</b></div><div class="fee-note">Deadline is January 21, 2026 at 11:59 PM</div></div>
      <div class="fee"><div class="fee-title">Late / On-site Registration is <b>$50.00</b></div><div class="fee-note">Deadline is January 23, 2026 at 5:00 PM</div></div>
    </div>
    <div class="limit">Registration is limited to the first <b>750</b> wrestlers</div>
    <div class="limit-note">Non-CWL card holders will pay an additional $5.00 at weigh-ins</div>
  </div>

  <div class="abs band band--deep">
    <span class="weigh-tag">WEIGH-INS</span>
    <ul class="weigh-list">
      <li>January 23, 2026–5:00 PM to 7:00 PM <span>(Early weigh-ins –$10 cash due at scale)</span></li>
      <li>January 24, 2026–6:00 AM to 7:30 AM <span>(K-5, 6U, 8U, 10U)</span></li>
      <li>January 24, 2026–11:00 AM to 12:00 PM <span>(12 &amp; Under, MS, &amp; High School)</span></li>
    </ul>
    <p class="fine fine--1">Tenths are waived/dropped at weigh-ins, satellite weigh-ins will not be allowed, High school divisions are given 2 lbs. growth allowance. Custom medals will be given to the top 3 individual finishers in each bracket.</p>
    <p class="fine fine--2">Custom awards will be awarded to the top 4 teams, referee decisions will be final. Pine Ridge Athletics is not responsible for accidents, injuries, or theft during the Tournament.</p>
    <div class="admission"><span class="tag">ADMISSION</span>$10.00 per person</div>
    <div class="contact">
      <div class="contact-label">For more information, contact<br><span>Tournament Director Dale Porter</span></div>
      <svg width="14" height="14" viewBox="0 0 14 14"><circle cx="7" cy="7" r="6.5" fill="#d9962e"/><path d="M4.6 3.8l1.3-.3.8 1.8-.9.7c.4.9 1.1 1.6 2 2l.7-.9 1.8.8-.3 1.3c-2.9.2-5.6-2.5-5.4-5.4z" fill="#430a0d"/></svg>
      <div class="contact-phone">(555) 214-0760</div>
    </div>
    <div class="hotels-title">Hotels available on-site</div>
    <div class="hotels">
      <span class="h-name">Lakeside Inn</span><span>(555) 355-5000</span>
      <span class="h-name">Maple Suites</span><span>(555) 355-7400</span>
      <span class="h-name">Cedar Lodge</span><span>(555) 355-8300</span>
    </div>
  </div>

  <div class="abs strip"></div>

  <div class="abs open-badge"><span class="o1">Open</span><span class="o2">18+</span></div>
</section>

<section class="page page--back">
  <div class="abs title-block">
    <div class="headline-top">8TH ANNUAL</div>
    <div class="headline-sub" style="margin-top:1px">RIDGEBACK CLASH</div>
  </div>

  <div class="abs panel"></div>
  <div class="abs panel-title"><b>2025-2026</b> CWL AGE &amp; WEIGHT CLASSES</div>

  <div class="col" style="left:57px"><div class="cell-num">DIVISION</div><div class="cell-label cell-label--first">Excluding the High School &amp; Open Division 12/31/2025</div>
    <div class="cells"><span class="blank"></span><span class="blank"></span><span class="blank"></span><span class="blank"></span><span class="blank"></span><span class="blank"></span></div></div>
  <div class="col" style="left:93.5px"><div class="cell-num">1</div><div class="cell-label">6 &amp; Under</div>
    <div class="cells"><span>36</span><span>40</span><span>44</span><span>48</span><span>52</span><span>56</span><span>60</span><span>HWT</span></div></div>
  <div class="col" style="left:130px"><div class="cell-num">2</div><div class="cell-label">8 &amp; Under</div>
    <div class="cells"><span>40</span><span>44</span><span>48</span><span>52</span><span>56</span><span>60</span><span>64</span><span>68</span><span>72</span><span>76</span><span>80</span><span>84</span><span>88</span><span>92</span><span>HWT</span></div></div>
  <div class="col" style="left:166.5px"><div class="cell-num">3</div><div class="cell-label">10 &amp; Under</div>
    <div class="cells"><span>52</span><span>55</span><span>60</span><span>64</span><span>68</span><span>72</span><span>76</span><span>80</span><span>84</span><span>88</span><span>92</span><span>96</span><span>100</span><span>110</span><span>HWT</span></div></div>
  <div class="col" style="left:203px"><div class="cell-num">4</div><div class="cell-label">12 &amp; Under</div>
    <div class="cells"><span>68</span><span>72</span><span>76</span><span>83</span><span>90</span><span>98</span><span>106</span><span>113</span><span>120</span><span>126</span><span>132</span><span>138</span><span>144</span><span>150</span><span>157</span><span>165</span><span>175</span><span>190</span><span>HWT</span></div></div>
  <div class="col" style="left:239.5px"><div class="cell-num">5</div><div class="cell-label">Middle School</div>
    <div class="cells"><span>76</span><span>83</span><span>90</span><span>98</span><span>106</span><span>113</span><span>120</span><span>126</span><span>132</span><span>138</span><span>144</span><span>150</span><span>157</span><span>165</span><span>175</span><span>190</span><span>215</span><span>HWT</span></div></div>
  <div class="col" style="left:276px"><div class="cell-num">6</div><div class="cell-label">Girls K-5</div>
    <div class="cells"><span>40</span><span>44</span><span>48</span><span>52</span><span>56</span><span>60</span><span>64</span><span>68</span><span>72</span><span>76</span><span>80</span><span>84</span><span>88</span><span>92</span><span>96</span><span>100</span><span>110</span><span>120</span><span>130</span></div></div>
  <div class="col" style="left:312.5px"><div class="cell-num">7</div><div class="cell-label">Girls 6th-8th</div>
    <div class="cells"><span>76</span><span>83</span><span>90</span><span>98</span><span>106</span><span>113</span><span>120</span><span>126</span><span>132</span><span>138</span><span>144</span><span>150</span><span>157</span><span>165</span><span>175</span><span>190</span><span>215</span><span>HWT</span></div></div>
  <div class="col" style="left:349px"><div class="cell-num">8</div><div class="cell-label">Women's Grades 9-12</div>
    <div class="cells"><span>100</span><span>107</span><span>114</span><span>120</span><span>126</span><span>132</span><span>145</span><span>152</span><span>165</span><span>185</span><span>235</span></div></div>
  <div class="col" style="left:385.5px"><div class="cell-num">9</div><div class="cell-label">High School Grades 9-12</div>
    <div class="cells"><span>106</span><span>113</span><span>120</span><span>126</span><span>132</span><span>138</span><span>144</span><span>150</span><span>157</span><span>165</span><span>175</span><span>190</span><span>215</span><span>285</span></div></div>
  <div class="col" style="left:422px"><div class="cell-num">10</div><div class="cell-label">Open 18+</div>
    <div class="cells"><span>125</span><span>133</span><span>141</span><span>149</span><span>157</span><span>165</span><span>174</span><span>184</span><span>197</span><span>215</span><span>285</span></div></div>

  <div class="abs photo photo--mats" role="img" aria-label="Overhead view of six wrestling mats in an arena"></div>
  <div class="abs band--award"></div>
  <div class="abs photo photo--back" role="img" aria-label="Armored warrior with crested helmet and spear"></div>
  <div class="abs award-text">Custom singlets are awarded to champions in all weight classes, <span>excluding the High School and Open Division.</span></div>
  <div class="abs singlet singlet--a" role="img" aria-label="Custom champion singlet, light design"></div>
  <div class="abs singlet singlet--b" role="img" aria-label="Custom champion singlet, dark design"></div>
</section>

</body>
</html>
```